Visitenkartenerstellung für Dorvek-Estates
Zielgruppe
Männer und Frauen, junge Familien bis hin zum Senior.
Verkauf von hochwertigen Immobilien in Spanien.
Aufgabenstellung
Auf Grund unserer Namensänderung benötigen wir ein neues Visitenkartendesign.
Wir sind eine skandinavische Agentur für Luxus-Immobilien auf Mallorca.
Das Design sollte dementsprechend edel aber dennoch schlicht gestaltet sein!

```html
<!DOCTYPE html>
<html lang="de">
<head>
<meta charset="utf-8">
<title>Dorvek-Estates – Visitenkarte</title>
<link rel="stylesheet" href="https://fonts.googleapis.com/css2?family=Lato:wght@300;400;700&display=swap">
<style>
  :root {
    --stage: #ececec;
    --card: #ffffff;
    --card-edge: #8a8a8a;
    --band-strong: #5b7a87;
    --band-mid: #9bb0b8;
    --band-fade: rgba(255, 255, 255, 0);
    --text-light: #ffffff;
    --text-dark: #2e2e2e;
    --text-muted: #4a4f53;
  }
  html, body {
    margin: 0;
    padding: 0;
    overflow: hidden;
  }
  body {
    width: 1200px;
    height: 754px;
    background: var(--stage);
    position: relative;
    font-family: "Lato", sans-serif;
  }
  .card {
    position: absolute;
    width: 483px;
    height: 311px;
    background: var(--card);
    border: 1px solid var(--card-edge);
    box-sizing: border-box;
    overflow: hidden;
  }
  .card--front { left: 178px; top: 139px; }
  .card--back  { left: 593px; top: 338px; }

  .band {
    position: absolute;
    left: 0;
    width: 100%;
    background: linear-gradient(90deg, var(--band-strong) 0%, var(--band-mid) 45%, var(--band-fade) 100%);
  }
  .card--front .band { top: 68px; height: 101px; }
  .card--back .band  { top: 61px; height: 98px; }

  .company-name {
    position: absolute;
    left: 42px;
    top: 22px;
    margin: 0;
    font-weight: 400;
    font-size: 26px;
    line-height: 1;
    color: var(--text-dark);
  }
  .tagline {
    position: absolute;
    left: 42px;
    top: 172px;
    margin: 0;
    font-weight: 400;
    font-size: 17px;
    color: var(--text-dark);
  }

  .person {
    position: absolute;
    left: 111px;
    top: 122px;
    margin: 0;
    display: flex;
    align-items: baseline;
    gap: 16px;
  }
  .person__name {
    font-weight: 700;
    font-size: 18px;
    color: var(--text-light);
  }
  .person__role {
    font-weight: 400;
    font-size: 15px;
    color: var(--text-muted);
  }
  .contact {
    position: absolute;
    left: 111px;
    top: 190px;
    margin: 0;
    font-style: normal;
    font-weight: 300;
    font-size: 15px;
    line-height: 20.5px;
    color: var(--text-muted);
  }
  .contact span { display: block; white-space: nowrap; }
</style>
</head>
<body>
  <section class="card card--front" aria-label="Vorderseite">
    <p class="company-name">Dorvek-Estates</p>
    <div class="band"></div>
    <p class="tagline">Luxury Real Estate on Mallorca &amp; Ibiza</p>
  </section>

  <section class="card card--back" aria-label="Rückseite">
    <div class="band"></div>
    <p class="person">
      <span class="person__name">Linnea Haglund</span>
      <span class="person__role">Property Manager</span>
    </p>
    <address class="contact">
      <span>C. Costa Serena 14 · 07950 Portals Spain</span>
      <span>Tel. 971 555 018 · Mobil 0034 600 555 241</span>
      <span>Linnea.Haglund@dorvek-estates.com</span>
      <span>www.dorvek-estates.se</span>
    </address>
  </section>
</body>
</html>
```